Website Design for a New Business Sharing Application

Purpose: Website for a new product – a sharing application called "Pondly.io"

Product concept: Easy sharing of business information. The application has different sections: tasks, calendars, documents, contacts, notes and links. The key feature of the application is that you can drag and drop information from different sections into a "share." A share is a page which lists all the types of information that you drag into it. You can add people to this "share."

Note: The application itself is not part of this project, just the website.

Website details: The site, in addition to being informational, will actually be the first point of entry for visitors into the application itself. Because of that, we would like the website design to reflect the look of the application, to create a smooth and seamless experience for the user moving from the website into the application (tough the website does not need to look *exactly* like the application). Included Product Tour screenshots show you the look of the application.

Website pages to be created: 4 pages
We are flexible in terms of the exact structure and placement of elements. You may change that any way you like. The pages are as follows:

Home page
Product Tour page
Press page
Blog page

Specific description of pages are provided in project files we will upload. We will also upload the logo, home page layout we have in mind, and other supporting files.

NOTE: Please submit first the design of the home page. Based on this design we will ask selected designers to submit designs for the other pages.

Target Market(s)

Business people who want to share work related files with their colleagues

Industry/Entity Type

Business

Requirements
Must have
• All the required features are listed in the description of the website and specific pages that we will upload.

```html
<!DOCTYPE html>
<html lang="en">
<head>
<meta charset="utf-8">
<title>Pondly.io – Share Now</title>
<link rel="stylesheet" href="https://fonts.googleapis.com/css2?family=Open+Sans:wght@400;600;700&family=Gochi+Hand&display=swap">
<style>
  :root {
    --bar-dark: #0b0b0b;
    --bar-mid: #222;
    --orange: #f29a1f;
    --orange-dark: #e07d10;
    --orange-text: #ec8a12;
    --blue-light: #3f97d0;
    --blue: #2a7fc0;
    --blue-deep: #0f5a9c;
    --icon-blue: #1f68a8;
    --white: #ffffff;
    --ink: #333333;
    --muted: #666666;
    --rule: #cfcfcf;
    --link: #1e6cb0;
  }
  * { box-sizing: border-box; margin: 0; padding: 0; }
  html, body { width: 1200px; height: 675px; overflow: hidden; background: #fff; }
  body { font-family: "Open Sans", Arial, sans-serif; position: relative; }

  .stripe { position: absolute; top: 0; left: 0; width: 1200px; height: 2px;
    background: linear-gradient(90deg, #999 0 15%, #e07d3c 15% 25%, #c14b8a 25% 32%, #6cb33f 32% 37%, #2aa7d8 37% 47%, #e5492d 47% 55%, #8a5ab5 55% 60%, #f3b71c 60% 68%, #2a7fc0 68% 75%, #c14b8a 75% 80%, #fff 80%); }

  .top-bar { position: absolute; top: 2px; left: 0; width: 1200px; height: 55px;
    background: linear-gradient(#1e1e1e, var(--bar-dark)); border-bottom: 1px solid #444; }
  .brand { position: absolute; left: 182px; top: 14px; display: flex; align-items: center; gap: 6px;
    color: var(--white); font-weight: 700; font-size: 21px; letter-spacing: -0.3px; }
  .brand-dot { width: 22px; height: 22px; border-radius: 50%; background: var(--orange-dark); }
  .login-btn { position: absolute; left: 895px; top: 12px; width: 126px; height: 29px; border-radius: 3px;
    background: linear-gradient(#f7aa36, var(--orange-dark)); color: var(--white); font-size: 13px; font-weight: 600;
    display: flex; align-items: center; justify-content: center; gap: 6px; }
  .login-btn::after { content: ""; border-left: 4px solid #fff; border-top: 3px solid transparent; border-bottom: 3px solid transparent; }

  .hero { position: absolute; top: 58px; left: 0; width: 1200px; height: 388px;
    background: radial-gradient(ellipse 60% 70% at 50% 25%, var(--blue-light), var(--blue) 60%, var(--blue-deep)); }
  .hero-deco { position: absolute; top: 100px; width: 230px; height: 110px; border-radius: 50%;
    background: radial-gradient(ellipse, rgba(10,50,100,0.25), rgba(10,50,100,0) 70%); }
  .hero-deco.left { left: 215px; }
  .hero-deco.right { left: 755px; }
  .hero-title { position: absolute; top: 72px; width: 100%; text-align: center; font-size: 41px; font-weight: 700;
    color: #e9edf2; letter-spacing: -1px; text-shadow: 0 2px 3px rgba(0,0,0,0.35); }
  .hero-title .now { color: var(--orange); }
  .hero-sub { position: absolute; top: 118px; width: 100%; text-align: center; font-size: 16px; font-weight: 600; color: var(--white); }
  .type-icons { position: absolute; top: 152px; left: 497px; display: flex; gap: 11px; }
  .type-icons svg { width: 19px; height: 19px; }

  .drop-zone { position: absolute; left: 182px; top: 234px; width: 305px; height: 97px;
    border: 3px dashed rgba(255,255,255,0.75); background: rgba(255,255,255,0.22);
    display: flex; align-items: center; color: var(--white); font-size: 14.5px; line-height: 20px; }
  .drop-zone .plus { font-size: 34px; font-weight: 400; width: 86px; text-align: center; }
  .divider-or { position: absolute; left: 590px; top: 230px; width: 22px; height: 102px; text-align: center; color: var(--white); }
  .divider-or .dots { height: 36px; border-left: 1px dotted rgba(255,255,255,0.8); margin: 0 auto; width: 0; }
  .divider-or .word { font-size: 20px; line-height: 30px; }
  .email-input { position: absolute; left: 713px; top: 233px; width: 308px; height: 45px; background: var(--white);
    border-radius: 3px; color: #999; font-size: 16px; padding: 11px 15px; }
  .start-btn { position: absolute; left: 713px; top: 286px; width: 308px; height: 45px; border-radius: 3px;
    background: linear-gradient(#fbb23f, var(--orange-dark)); color: var(--white); font-size: 21px; font-weight: 600;
    display: flex; align-items: center; justify-content: center; text-shadow: 0 1px 1px rgba(0,0,0,0.2); }

  .features { position: absolute; top: 446px; left: 0; width: 1200px; height: 170px;
    background: linear-gradient(#ececec, #fff 60px); }
  .feature { position: absolute; top: 32px; width: 260px; margin-left: -130px; text-align: center; }
  .feature svg { width: 38px; height: 38px; display: block; margin: 0 auto; }
  .feature h2 { font-size: 17px; font-weight: 700; color: var(--ink); margin-top: 8px; }
  .feature h2 .free { color: var(--orange-text); }
  .feature p { font-size: 11.5px; color: var(--muted); line-height: 16px; margin-top: 6px; }
  .feature a { color: var(--link); text-decoration: none; }

  .footer-rule { position: absolute; top: 616px; left: 178px; width: 844px; border-top: 1px solid var(--rule); }
  .footer-note { position: absolute; top: 624px; left: 325px; font-family: "Gochi Hand", cursive; font-size: 13px; color: var(--muted); }
  .footer-note .free { color: var(--orange-text); }
  .footer-links { position: absolute; top: 646px; left: 178px; font-size: 11px; color: #444; }
  .footer-links s { color: #444; }
  .copyright { position: absolute; top: 646px; left: 785px; font-size: 11px; color: #444; }
  .social { position: absolute; top: 646px; left: 948px; display: flex; gap: 8px; font-size: 10px; color: #888; font-weight: 600; }
</style>
</head>
<body>
  <div class="stripe"></div>

  <header class="top-bar">
    <div class="brand"><span class="brand-dot"></span>Pondly.io</div>
    <div class="login-btn">Login to shares</div>
  </header>

  <section class="hero">
    <div class="hero-deco left" role="img" aria-label="Faint cluster of file, image and calendar icons"></div>
    <div class="hero-deco right" role="img" aria-label="Faint cluster of file, image and calendar icons"></div>
    <h1 class="hero-title">Share <span class="now">NOW</span></h1>
    <p class="hero-sub">Drag information, add people, BOOM!</p>
    <div class="type-icons">
      <svg viewBox="0 0 20 20" fill="#fff"><rect x="2" y="2" width="10" height="12"/><rect x="7" y="7" width="10" height="12" stroke="#2a7fc0" stroke-width="1.5"/></svg>
      <svg viewBox="0 0 20 20"><rect x="1.5" y="3" width="17" height="14" fill="none" stroke="#fff" stroke-width="2"/><path d="M3 16 L8 9 L12 13 L14 11 L17 16Z" fill="#fff"/><circle cx="14" cy="7" r="1.6" fill="#fff"/></svg>
      <svg viewBox="0 0 20 20"><rect x="2" y="3" width="15" height="15" rx="2" fill="none" stroke="#fff" stroke-width="2"/><path d="M5 10 L9 14 L18 4" fill="none" stroke="#fff" stroke-width="2.6"/></svg>
      <svg viewBox="0 0 20 20" fill="#fff"><rect x="1" y="3" width="3" height="3"/><rect x="6" y="3" width="13" height="3"/><rect x="1" y="9" width="3" height="3"/><rect x="6" y="9" width="13" height="3"/><rect x="1" y="15" width="3" height="3"/><rect x="6" y="15" width="13" height="3"/></svg>
      <svg viewBox="0 0 20 20"><rect x="3" y="1" width="14" height="18" fill="#fff"/><path d="M6 5h8M6 8h8M6 11h8M6 14h8" stroke="#2a7fc0" stroke-width="1.2"/></svg>
      <svg viewBox="0 0 20 20"><rect x="1.5" y="3" width="17" height="15" fill="none" stroke="#fff" stroke-width="2"/><rect x="1.5" y="3" width="17" height="4" fill="#fff"/><text x="10" y="16" font-size="7" fill="#fff" text-anchor="middle" font-family="Arial, sans-serif">12</text></svg>
      <svg viewBox="0 0 20 20"><circle cx="10" cy="10" r="9" fill="#fff"/><path d="M5 6 Q8 5 9 8 Q8 11 6 11 Q5 14 7 16 M12 4 Q15 7 13 9 Q15 12 16 13" fill="none" stroke="#2a7fc0" stroke-width="2"/></svg>
    </div>

    <div class="drop-zone"><span class="plus">+</span><span>Drag Files Here to Share<br>Immediately</span></div>
    <div class="divider-or"><div class="dots"></div><div class="word">or</div><div class="dots"></div></div>
    <div class="email-input">Enter business email...</div>
    <div class="start-btn">Start Sharing</div>
  </section>

  <section class="features">
    <div class="feature" style="left:320px">
      <svg viewBox="0 0 40 40"><circle cx="20" cy="20" r="19" fill="var(--icon-blue)"/><text x="20" y="29" font-size="26" font-weight="700" fill="#fff" text-anchor="middle" font-family="Open Sans, Arial, sans-serif">?</text></svg>
      <h2>What is it?</h2>
      <p>Lorem ipsum dolor sit amet, consectetuer<br>adipiscing elit, sed diam <a href="#">Readmore</a></p>
    </div>
    <div class="feature" style="left:594px">
      <svg viewBox="0 0 40 40"><path d="M2 6 L36 2 L37 9 L3 13Z" fill="var(--icon-blue)"/><path d="M9 5l3 6M17 4l3 6M25 3l3 6" stroke="#fff" stroke-width="2"/><rect x="2" y="15" width="36" height="23" fill="var(--icon-blue)"/></svg>
      <h2>Watch Video</h2>
      <p>Lorem ipsum dolor sit amet, consectetuer<br>adipiscing elit, sed diam <a href="#">Readmore</a></p>
    </div>
    <div class="feature" style="left:869px">
      <svg viewBox="0 0 40 40"><polygon fill="var(--icon-blue)" points="20,0 23,4 27,1 29,6 34,4 34,9 39,10 36,14 40,18 36,21 39,26 34,27 34,32 29,31 27,36 23,33 20,38 17,33 13,36 11,31 6,32 6,27 1,26 4,21 0,18 4,14 1,10 6,9 6,4 11,6 13,1 17,4"/><circle cx="20" cy="19" r="14" fill="none" stroke="#fff" stroke-width="0.8" stroke-dasharray="1.5 1.5"/><text x="20" y="22" font-size="9" font-weight="700" fill="#fff" text-anchor="middle" font-family="Open Sans, Arial, sans-serif">FREE</text></svg>
      <h2><span class="free">FREE</span> for Unlimited Users</h2>
      <p>Lorem ipsum dolor sit amet, consectetuer<br>adipiscing elit, sed diam <a href="#">Readmore</a></p>
    </div>
  </section>

  <footer>
    <div class="footer-rule"></div>
    <div class="footer-note"><span class="free">Free</span> for Unlimited Users</div>
    <nav class="footer-links">Home | About us | Product Tour | <s>Pricing</s> | Terms of use | Sign up | Blog | Contact us</nav>
    <div class="copyright">Copyright © 2012 Pondly.io</div>
    <div class="social"><span>Sociable</span><span>Chatter</span><span>Orbit</span></div>
  </footer>
</body>
</html>
```